Speisekarten-Design für Biergarten am Ufer des Bodensees
Super tolle Designerin. Vielen Dank Roswitha!
Zielgruppe
Wir sind ein direkt am Ufer des Bodensees liegender Biergarten, welcher seit über 30 Jahren besteht und deshalb fest in unserer Stadt verwurzelt ist. Zu unserer Zielgruppe gehören Touristen und Einheimische jeglicher Art - wir heißen einfach alle willkommen. Wir bieten unseren Gästen einfache Speisen und lokale Getränke. Uns ist wichtig, dass die Speise- & Getränkekarte das Gefühl von Heimat, Regionalität und Liebe zum Bodensee vermittelt. Wir bevorzugen ein modernes und klares Design, welches jedoch klassische Strukturen wie die eines typischen 60er-Jahre-Diners miteinbezieht.
Aufgabenstellung
Es wäre es toll, wenn diese Faltbar und kompakt (DIN-A4 evtl. etwas größer) ist. Die Textfelder sollten das komplette Speise- und Getränkeangebot darstellen (ca. 15 Gerichte, 6 Biersorten, 6 Softdrinks, 6 Heißgetränke). Wir bevorzugen warme Farbtöne. Es ist nicht notwendig Bilder in der Karte zu hinterlegen.

```html
<!DOCTYPE html>
<html lang="de">
<head>
<meta charset="utf-8">
<title>Hanni's Pavillon am Ufer – Speisekarte</title>
<link rel="stylesheet" href="https://fonts.googleapis.com/css2?family=Open+Sans:wght@400;600;700&display=swap">
<style>
:root{
  --paper:#fbf8ec;
  --teal:#1b7796;
  --ink:#2b2b2b;
  --hop:#a9a9a9;
  --hop-faint:#efeadb;
  --frame:#cfcfcf;
  --stage:#ffffff;
}
*{margin:0;padding:0;box-sizing:border-box}
html,body{width:1200px;height:426px;overflow:hidden;background:var(--stage)}
body{position:relative;font-family:"Open Sans",Arial,sans-serif;color:var(--ink)}
.panel{position:absolute;top:20px;height:386px;background:var(--paper);border:1px solid var(--frame)}
.cover{left:22px;width:277px}
.spread{left:325px;width:549px}
.back{left:901px;width:277px}

.hop-pattern{position:absolute;left:18px;top:28px;width:241px;height:330px;border-radius:6px;
  background:radial-gradient(circle,var(--hop) 0 7px,transparent 8px) 0 0/42.5px 53px;opacity:.7}
.cover-seal{position:absolute;left:60px;top:113px;width:157px;height:157px;border-radius:50%;background:var(--teal);
  display:flex;align-items:center;justify-content:center;text-align:center}
.cover-name{color:var(--paper);font-weight:700;font-size:17px;line-height:20px;width:120px}

.leaf-backdrop{position:absolute;border-radius:50%;background:radial-gradient(ellipse,var(--hop-faint),transparent 70%)}
.fold{position:absolute;left:274px;top:0;height:100%;border-left:1px dashed #d9d4c3}
.section-title{position:absolute;color:var(--teal);font-weight:600;font-size:16px;letter-spacing:3px;
  transform-origin:left top;transform:rotate(-90deg);white-space:nowrap}
.rule{position:absolute;border-left:1.5px dotted var(--teal)}
.menu-col{position:absolute;width:93px}
.dish{margin-bottom:6.5px}
.dish-head{display:flex;align-items:baseline;font-size:6.2px;line-height:8px}
.dish-name{color:var(--teal);font-weight:700}
.leader{flex:1;border-bottom:.6px dotted #777;margin:0 1px;transform:translateY(-1.5px)}
.dish-text{font-size:5.1px;line-height:7.1px}
.dish-text sup{font-size:3.5px}

.drinks{position:absolute;left:327px;width:92px}
.drink-block{margin-bottom:10px}
.drink-head{display:flex;font-size:6.2px;line-height:8px;padding-bottom:3px;border-bottom:1.5px dotted var(--teal);margin-bottom:4px}
.drink-head .dish-name{flex:1}
.drink-head i{font-style:italic;width:18px;text-align:right}
.drink{display:flex;align-items:baseline;font-size:5.3px;line-height:9.2px;font-weight:600}
.drink .price{font-weight:400}
.legend{position:absolute;left:451px;top:211px;width:70px;font-size:4.3px;line-height:7.2px}
.legend h3{font-size:4.6px;font-weight:700;line-height:8px}
.legend hr{border:0;border-top:.6px solid #bbb;margin:4px 0}
.hop-cell{position:absolute;width:20px;height:30px;border-radius:40% 40% 48% 48%;background:var(--hop);opacity:.75}
.footer-note{position:absolute;top:354px;font-size:4.4px;letter-spacing:1.2px;font-weight:700;color:#d6d0bd}

.back-name{position:absolute;top:162px;left:0;width:100%;text-align:center;color:var(--teal);font-size:6.6px;font-weight:700;letter-spacing:.4px}
.back-rule{position:absolute;left:96px;width:85px;border-top:1.5px dotted var(--teal)}
.back-info{position:absolute;top:183px;left:0;width:100%;text-align:center;font-size:5.2px;line-height:10px}
</style>
</head>
<body>

<section class="panel cover">
  <div class="hop-pattern" role="img" aria-label="Muster aus gezeichneten Hopfendolden in Grau"></div>
  <div class="cover-seal"><p class="cover-name">Hanni's Pavillon am Ufer</p></div>
</section>

<section class="panel spread">
  <div class="leaf-backdrop" style="left:160px;top:-20px;width:240px;height:130px" role="img" aria-label="Blasse Hopfendolde als Hintergrund"></div>
  <div class="leaf-backdrop" style="left:-10px;top:270px;width:220px;height:130px" role="img" aria-label="Blasse Hopfendolde als Hintergrund"></div>
  <div class="leaf-backdrop" style="left:360px;top:270px;width:200px;height:130px" role="img" aria-label="Blasse Hopfendolde als Hintergrund"></div>
  <div class="fold"></div>

  <h2 class="section-title" style="left:19px;top:168px">GERICHTE</h2>
  <div class="rule" style="left:40px;top:63px;height:284px"></div>

  <div class="menu-col" style="left:49px;top:63px">
    <div class="dish"><div class="dish-head"><span class="dish-name">Toast Hawaii</span><span class="leader"></span>4.50</div><p class="dish-text">Lorem ipsum<sup>[1]</sup> dolor amet, consectetur adipiscing elit, sed do eiusmod tempor incididunt ut labore et dolore sed do eismund adipiscing</p></div>
    <div class="dish"><div class="dish-head"><span class="dish-name">Grillteller</span><span class="leader"></span>7.50</div><p class="dish-text">Ut enim ad minim<sup>[C]</sup> veniam, quis nostrud exercitation ullamco laboris</p></div>
    <div class="dish"><div class="dish-head"><span class="dish-name">Gemischter Salat</span><span class="leader"></span>4.50</div><p class="dish-text">Ut enim ad minim veniam<sup>[2,G]</sup>, quis nostrud exercitation ullamco laboris nisi ut<sup>[3]</sup> aliquip ex ea commodo consequat nisi ut lorem ipsum</p></div>
    <div class="dish"><div class="dish-head"><span class="dish-name">Wurstteller</span><span class="leader"></span>4.00</div><p class="dish-text">Lorem ipsum dolor sit, consectetur adipiscing elit, sed do eiusmod</p></div>
    <div class="dish"><div class="dish-head"><span class="dish-name">Toast Hawaii</span><span class="leader"></span>4.50</div><p class="dish-text">Lorem ipsum dolor amet, consectetur adipiscing elit, sed do eiusmod tempor incididunt ut labore aliqua</p></div>
    <div class="dish"><div class="dish-head"><span class="dish-name">Grillteller</span><span class="leader"></span>7.50</div><p class="dish-text">Ut enim ad minim veniam, quis nostrud exercitation ullamco laboris nisi ut aliquip ex ea commodo</p></div>
    <div class="dish"><div class="dish-head"><span class="dish-name">Gemischter Salat</span><span class="leader"></span>4.50</div><p class="dish-text">Ut enim ad minim veniam, quis nostrud exercitation ullamco laboris nostrud exercitation</p></div>
    <div class="dish"><div class="dish-head"><span class="dish-name">Grillteller</span><span class="leader"></span>7.50</div><p class="dish-text">Ut enim ad minim veniam, quis nostrud exercitation ullamco laboris nisi ut aliquip ex ea commodo</p></div>
  </div>

  <div class="menu-col" style="left:159px;top:63px">
    <div class="dish"><div class="dish-head"><span class="dish-name">Toast Hawaii</span><span class="leader"></span>4.50</div><p class="dish-text">Lorem ipsum<sup>[C]</sup> dolor amet, consectetur adipiscing elit, sed do eiusmod</p></div>
    <div class="dish"><div class="dish-head"><span class="dish-name">Grillteller</span><span class="leader"></span>7.50</div><p class="dish-text">Ut enim ad minim veniam, quis nostrud exercitation ullamco laboris nisi ut aliquip ex ea commodo</p></div>
    <div class="dish"><div class="dish-head"><span class="dish-name">Gemischter Salat</span><span class="leader"></span>4.50</div><p class="dish-text">Ut enim ad minim veniam, quis nostrud exercitation ullamco laboris nisi ut aliquip ex ea commodo consequat nisi ut lorem ipsum</p></div>
    <div class="dish"><div class="dish-head"><span class="dish-name">Wurstteller</span><span class="leader"></span>4.00</div><p class="dish-text">Lorem ipsum dolor sit, consectetur adipiscing elit, sed do eiusmod</p></div>
    <div class="dish"><div class="dish-head"><span class="dish-name">Grillteller</span><span class="leader"></span>7.50</div><p class="dish-text">Ut enim ad minim veniam, quis nostrud exercitation ullamco laboris nisi ut aliquip ex ea commodo</p></div>
    <div class="dish"><div class="dish-head"><span class="dish-name">Toast Hawaii</span><span class="leader"></span>4.50</div><p class="dish-text">Lorem ipsum dolor amet, consectetur adipiscing elit, sed do eiusmod tempor incididunt ut labore aliqua</p></div>
    <div class="dish"><div class="dish-head"><span class="dish-name">Gemischter Salat</span><span class="leader"></span>4.50</div><p class="dish-text">Ut enim ad minim veniam, quis nostrud exercitation ullamco laboris nisi ut aliquip ex ea commodo consequat ullamco laboris nostrud</p></div>
    <div class="dish"><div class="dish-head"><span class="dish-name">Grillteller</span><span class="leader"></span>7.50</div><p class="dish-text">Ut enim ad minim veniam, quis nostrud exercitation ullamco laboris nisi ut aliquip ex ea commodo</p></div>
  </div>

  <h2 class="section-title" style="left:298px;top:176px">GETRÄNKE</h2>
  <div class="rule" style="left:318px;top:63px;height:284px"></div>
  <div class="rule" style="left:431px;top:63px;height:284px"></div>

  <div class="drinks" style="top:61px">
    <div class="drink-block">
      <div class="drink-head"><span class="dish-name">Etwas Heisses</span><i>0.2l</i><i>0.5l</i></div>
      <div class="drink">KAFFEE<span class="leader"></span><span class="price">€ 2.50 … € 4.00</span></div>
      <div class="drink">MILCHKAFFEE<span class="leader"></span><span class="price">€ 2.50 … € 4.00</span></div>
      <div class="drink">TEEKANNE<span class="leader"></span><span class="price">€ 2.50 … € 4.00</span></div>
      <div class="drink">MALZDRINK<span class="leader"></span><span class="price">€ 2.50 … € 4.00</span></div>
      <div class="drink">GROG<span class="leader"></span><span class="price">€ 2.50 … € 4.00</span></div>
      <div class="drink">SCHOKOLADE<span class="leader"></span><span class="price">€ 2.50 … € 4.00</span></div>
    </div>
    <div class="drink-block">
      <div class="drink-head"><span class="dish-name">Etwas Kaltes</span><i>0.2l</i><i>0.5l</i></div>
      <div class="drink">KOLA CLASSIC<span class="leader"></span><span class="price">€ 2.50 … € 4.00</span></div>
      <div class="drink">ZITROLIMO<span class="leader"></span><span class="price">€ 2.50 … € 4.00</span></div>
      <div class="drink">ORANGENLIMO<span class="leader"></span><span class="price">€ 2.50 … € 4.00</span></div>
      <div class="drink">SEEQUELLE<span class="leader"></span><span class="price">€ 2.50 … € 4.00</span></div>
      <div class="drink">GINGER ALE<span class="leader"></span><span class="price">€ 2.50 … € 4.00</span></div>
      <div class="drink">TONIC WATER<span class="leader"></span><span class="price">€ 2.50 … € 4.00</span></div>
    </div>
    <div class="drink-block">
      <div class="drink-head"><span class="dish-name">Fassbier</span><i>0.3l</i><i>0.5l</i></div>
      <div class="drink">LAGER<span class="leader"></span><span class="price">€ 2.50 … € 4.00</span></div>
      <div class="drink">DRAFT<span class="leader"></span><span class="price">€ 2.50 … € 4.00</span></div>
      <div class="drink">NORDHELL<span class="leader"></span><span class="price">€ 2.50 … € 4.00</span></div>
      <div class="drink">STOUT<span class="leader"></span><span class="price">€ 2.50 … € 4.00</span></div>
    </div>
    <div class="drink-block">
      <div class="drink-head"><span class="dish-name">Flaschenbier</span><i>0.33l</i></div>
      <div class="drink">GRÜNHOPF<span class="leader"></span><span class="price">€ 4.00</span></div>
      <div class="drink">SONNENBIER<span class="leader"></span><span class="price">€ 4.00</span></div>
      <div class="drink">WEIZENHOF<span class="leader"></span><span class="price">€ 4.00</span></div>
      <div class="drink">NORDHELL<span class="leader"></span><span class="price">€ 4.00</span></div>
    </div>
  </div>

  <div class="hop-cell" style="left:452px;top:64px" role="img" aria-label="Gezeichnete Hopfendolde"></div>
  <div class="hop-cell" style="left:494px;top:64px" role="img" aria-label="Gezeichnete Hopfendolde"></div>
  <div class="hop-cell" style="left:452px;top:112px" role="img" aria-label="Gezeichnete Hopfendolde"></div>
  <div class="hop-cell" style="left:494px;top:112px" role="img" aria-label="Gezeichnete Hopfendolde"></div>
  <div class="hop-cell" style="left:452px;top:162px" role="img" aria-label="Gezeichnete Hopfendolde"></div>
  <div class="hop-cell" style="left:494px;top:162px" role="img" aria-label="Gezeichnete Hopfendolde"></div>

  <div class="legend">
    <h3>ZUSATZSTOFFE</h3>
    <p>[1] = mit Farbstoff<br>[2] = mit Konservierungsstoff<br>[3] = mit Antioxidationsmittel<br>[4] = mit Geschmacksverstärker<br>[15] = koffeinhaltig<br>[3] = mit Antioxidationsmittel<br>[4] = mit Geschmacksverstärker<br>[15] = koffeinhaltig</p>
    <hr>
    <h3>ALLERGENE</h3>
    <p>[A] = Getreideprodukte (Gluten)<br>[B] = Schwefeldioxide<br>[C] = Eier<br>[D] = Fisch<br>[E] = Getreideprodukte (Gluten)<br>[G] = Schwefeldioxide</p>
  </div>

  <p class="footer-note" style="left:202px">SELBSTBEDIENUNGSRESTAURANT</p>
  <p class="footer-note" style="left:298px">HANNI'S PAVILLON AM UFER</p>
</section>

<section class="panel back">
  <div class="hop-cell" style="left:128px;top:114px" role="img" aria-label="Gezeichnete Hopfendolde"></div>
  <p class="back-name">HANNI'S PAVILLON AM UFER</p>
  <div class="back-rule" style="top:174px"></div>
  <p class="back-info">Liesel Auberger-Dorn &amp; Tobias Kernwald GbR<br>Seegasse 12, 78400 Uferstadt, Tel.: 07500-12345<br>www.hannis-pavillon-am-ufer.de</p>
  <div class="back-rule" style="top:214px"></div>
  <div class="hop-cell" style="left:128px;top:228px" role="img" aria-label="Gezeichnete Hopfendolde"></div>
</section>

</body>
</html>
```